Website Design for WeselneKarety.pl – Luxury Wedding Car Rental with Chauffeur

We are looking for a talented designer to create a modern, elegant, and fully responsive website for our new brand – WeselnyKarety.pl. We are a premium car rental platform in Poland, offering luxury and exotic vehicles exclusively for weddings. All cars come with a professional chauffeur, ensuring a high-end, stress-free, and stylish experience.
Website Purpose:
The website should present our offering in a luxurious, clear, and inspiring way. It must build trust, highlight the prestige of our brand, and encourage inquiries. Our target audience includes engaged couples, wedding planners, and clients seeking a truly exceptional vehicle for their special day.
Design Requirements:
Style: modern, elegant, minimalist
Color palette: white, black, gold, optionally silver – refined and luxurious
Typography: clean, modern, high-end
Layout: clear, intuitive, with large car images and well-defined sections
Fully responsive (desktop, tablet, mobile)
Bilingual layout (Polish/English) must be considered
Pages to Design:
Homepage
About Us
Fleet Overview
Individual Car Pages
Services (Weddings, Photo Shoots, Film Rentals)
Why Us / Unique Selling Points
Contact
FAQ
Inspiration:
Luxury automotive brands (e.g. Varnell-Dorne, Corwick, Elsby Havard)
High-end wedding websites
Minimalist layouts with large visuals and elegant typography
Additional Notes:
The design should evoke the emotions of a wedding day – elegance, uniqueness, style, and class. Please avoid flashy colors, excessive graphic effects, or overly decorative elements. Subtlety, prestige, and sophistication are key.

```html
<!DOCTYPE html>
<html lang="en">
<head>
<meta charset="utf-8">
<title>WeselneKarety.pl – Luxury Wedding Car Rental</title>
<link href="https://fonts.googleapis.com/css2?family=Playfair+Display:wght@900&family=Poppins:wght@400;500;600;700&display=swap" rel="stylesheet">
<style>
:root{
  --gold:#d4b85a;
  --ink:#111;
  --navy:#15233a;
  --paper:#f6f6f5;
  --white:#fff;
  --line:#5a6b82;
}
*{box-sizing:border-box;margin:0;padding:0}
html,body{width:1200px;height:2865px;overflow:hidden}
body{position:relative;background:var(--white);font-family:"Poppins",sans-serif;color:var(--ink)}
.abs{position:absolute}

.hero{left:0;top:0;width:1200px;height:892px;background:radial-gradient(ellipse at 70% 45%,#5b5b5b 0%,#2e2e2e 40%,#111 80%)}
.nav{left:83px;top:61px;width:1033px;height:90px;background:var(--white);border-radius:45px}
.nav-contact{left:32px;top:31px;width:80px;height:28px;border:1px solid var(--gold);border-radius:14px;font-size:12px;line-height:26px;text-align:center}
.nav-links{left:141px;top:37px;display:flex;gap:29px;font-size:12px;font-weight:500;list-style:none}
.nav-brand{right:40px;top:30px;font-family:"Poppins",sans-serif;font-weight:500;font-size:22px;color:var(--gold)}

.hero-title{left:172px;top:258px;font-family:"Playfair Display",serif;font-weight:900;font-size:62px;line-height:66px;color:var(--gold);letter-spacing:1px}
.hero-sub{left:172px;top:406px;font-size:28px;line-height:33px;color:var(--white)}
.hero-btn{left:172px;top:537px;width:170px;height:63px;border-radius:32px;background:var(--gold);color:var(--ink);font-size:18px;line-height:63px;text-align:center}
.chat{left:1032px;top:673px;width:84px;height:84px;border-radius:50%;background:var(--white)}

.about-pill{left:340px;top:846px;width:520px;height:90px;border-radius:45px;background:var(--white);box-shadow:0 6px 14px rgba(0,0,0,.15);text-align:center;font-family:"Playfair Display",serif;font-weight:900;font-size:50px;line-height:90px;color:var(--gold)}
.about-text{left:0;top:1006px;width:1200px;text-align:center;font-size:17.5px;line-height:29.2px}
.about-rule{left:277px;top:1279px;width:646px;height:1px;background:var(--line)}

.why{left:0;top:1402px;width:1200px;height:1109px;background:var(--paper)}
.why-title{left:83px;top:1592px;font-family:"Playfair Display",serif;font-weight:900;font-size:53px;color:var(--gold)}
.why-dash{left:83px;top:1706px;width:38px;height:6px;background:var(--navy)}
.why-text{left:83px;top:1768px;width:375px;font-size:17px;line-height:25px}
.card{left:503px;width:614px;height:142px;border-radius:71px;background:var(--white);box-shadow:0 4px 12px rgba(0,0,0,.12)}
.card-icon{left:38px;top:41px;width:62px;height:60px}
.card-divider{left:165px;top:21px;width:1px;height:100px;background:#ddd}
.card-title{left:207px;top:36px;font-size:17.5px;font-weight:700}
.card-text{left:207px;top:73px;font-size:17.5px;line-height:22px}

.brand-mark{left:0;top:2190px;width:1200px;text-align:center;font-family:"Poppins",sans-serif;font-weight:500;font-size:80px;color:var(--gold)}

.footer{left:0;top:2511px;width:1200px;height:286px;background:var(--navy)}
.banner{left:140px;top:2451px;width:920px;height:119px;border-radius:6px;background:linear-gradient(90deg,#1f2c42,#2e3b52 50%,#1f2c42);box-shadow:0 4px 10px rgba(0,0,0,.25)}
.banner-text{left:140px;top:2451px;width:920px;height:119px;text-align:center;font-family:"Playfair Display",serif;font-weight:900;font-size:40px;line-height:119px;letter-spacing:14px;color:var(--gold)}
.contact{top:2651px;color:var(--white);font-size:11.5px;line-height:22px;display:flex;gap:8px}
.contact svg{margin-top:5px;flex:none}
.socials{left:938px;top:2651px;display:flex;gap:16px;font-size:11px;color:var(--white)}
.legal{left:0;top:2797px;width:1200px;height:68px;background:var(--paper);font-size:12.5px}
.legal span{position:absolute;top:20px}
</style>
</head>
<body>

<div class="abs hero" role="img" aria-label="Black and white photo of a luxury wedding car front at night"></div>

<nav class="abs nav">
  <a class="abs nav-contact">Contact</a>
  <ul class="abs nav-links"><li>Home</li><li>About Us</li><li>Fleet Overview</li><li>Cars</li><li>Services</li><li>Why Us</li><li>FAQ</li></ul>
  <div class="abs nav-brand">Weselne Karety</div>
</nav>

<h1 class="abs hero-title">LUXURY WEDDING<br>CAR RENTAL</h1>
<p class="abs hero-sub">Exclusive cars<br>with chauffeur for your<br>special day</p>
<a class="abs hero-btn">View cars</a>

<svg class="abs" style="left:0;top:673px" width="760" height="84" viewBox="0 0 760 84">
  <polygon points="0,0 176,0 132,84 0,84" fill="#b49a4c" opacity=".85"/>
  <polygon points="208,0 465,0 420,84 164,84" fill="#9a9a9a" opacity=".8"/>
  <polygon points="497,0 752,0 707,84 452,84" fill="#8a7537" opacity=".8"/>
</svg>

<div class="abs chat">
  <svg class="abs" style="left:19px;top:22px" width="46" height="40" viewBox="0 0 46 40">
    <rect x="0" y="0" width="46" height="32" rx="7" fill="var(--gold)"/>
    <polygon points="10,30 22,30 12,40" fill="var(--gold)"/>
    <circle cx="13" cy="16" r="3.5" fill="#fff"/><circle cx="23" cy="16" r="3.5" fill="#fff"/><circle cx="33" cy="16" r="3.5" fill="#fff"/>
  </svg>
</div>

<h2 class="abs about-pill">ABOUT US</h2>
<p class="abs about-text">
Lorem Ipsum is simply dummy text of the printing and typesetting industry.<br>
Lorem Ipsum has been the industry's standard dummy text ever since the 1500s,<br>
when an unknown took a galley of type and scrambled it to make a type specimen.<br>
survived not only five centuries, but also the leap into electronic pesetting, remaining essentially unchanged.<br>
It was popularised in the 1960s with the release of Typeline sheets containing Lorem Ipsum passages,<br>
and more recently with desktop publishing software like Pagecraft Studio including versions of <b>Lorem Ipsum.</b>
</p>
<div class="abs about-rule"></div>

<section class="abs why"></section>
<h2 class="abs why-title">WHY US</h2>
<div class="abs why-dash"></div>
<p class="abs why-text">Lorem Ipsum is simply dummy text of the printing and typesetting industry. Lorem Ipsum has been the industry's standard dummy text ever since the 1500s, when an unknown took a galley of type and scrambled it to make a type specimen.</p>

<div class="abs card" style="top:1523px">
  <svg class="abs card-icon" viewBox="0 0 62 60"><path d="M7 40V30a24 24 0 0 1 48 0v10" fill="none" stroke="var(--gold)" stroke-width="6"/><rect x="3" y="32" width="12" height="20" rx="4" fill="var(--gold)"/><rect x="47" y="32" width="12" height="20" rx="4" fill="var(--gold)"/></svg>
  <div class="abs card-divider"></div>
  <h3 class="abs card-title">24/7 Support</h3>
  <p class="abs card-text">Lorem Ipsum is simply dummy text of the<br>printing and typesetting industry.</p>
</div>
<div class="abs card" style="top:1688px">
  <svg class="abs card-icon" viewBox="0 0 62 60"><path d="M14 3h24l12 12v40a2 2 0 0 1-2 2H14a2 2 0 0 1-2-2V5a2 2 0 0 1 2-2z" fill="none" stroke="var(--gold)" stroke-width="3.5"/><path d="M22 30h10M22 38h18M22 46h18" stroke="var(--gold)" stroke-width="3.5"/></svg>
  <div class="abs card-divider"></div>
  <h3 class="abs card-title">Affordable Cost</h3>
  <p class="abs card-text">Lorem Ipsum is simply dummy text of the<br>printing and typesetting industry.</p>
</div>
<div class="abs card" style="top:1855px">
  <svg class="abs card-icon" viewBox="0 0 62 60"><polygon points="4,10 30,30 4,50" fill="var(--gold)"/><polygon points="30,10 58,30 30,50" fill="var(--gold)"/></svg>
  <div class="abs card-divider"></div>
  <h3 class="abs card-title">Fast Delivery</h3>
  <p class="abs card-text">Lorem Ipsum is simply dummy text of the<br>printing and typesetting industry.</p>
</div>

<div class="abs brand-mark">Weselne Karety</div>

<footer class="abs footer"></footer>
<div class="abs banner" role="img" aria-label="Faint dark photo of a wedding couple behind the banner"></div>
<div class="abs banner-text">LET’S BE TOGETHER!</div>

<div class="abs contact" style="left:140px">
  <svg width="11" height="11" viewBox="0 0 24 24"><path d="M6 2l4 4-2.5 3a14 14 0 0 0 7.5 7.5L18 14l4 4-3 4C10 21 3 14 2 5z" fill="#fff"/></svg>
  <span>1-800-555-0142</span>
</div>
<div class="abs contact" style="left:396px">
  <svg width="12" height="10" viewBox="0 0 24 18"><rect x="1" y="1" width="22" height="16" rx="2" fill="none" stroke="#fff" stroke-width="2"/><path d="M1 2l11 8 11-8" fill="none" stroke="#fff" stroke-width="2"/></svg>
  <span>kontakt@weselnekarety.pl</span>
</div>
<div class="abs contact" style="left:647px">
  <svg width="11" height="13" viewBox="0 0 20 24"><path d="M10 23s8-8 8-13a8 8 0 0 0-16 0c0 5 8 13 8 13z" fill="none" stroke="#fff" stroke-width="2"/><circle cx="10" cy="10" r="3" fill="none" stroke="#fff" stroke-width="2"/></svg>
  <span>Aurelle Events, LLC<br>48 Marlow Lane Suite 2,<br>Fairbrook, TX 70001</span>
</div>
<div class="abs socials"><span>Vidora</span><span>Chirpline</span><span>Worknest</span></div>

<div class="abs legal">
  <span style="left:83px">© 2023 Welcome. All right reserved.</span>
  <span style="left:860px">Privacy Policy</span>
  <span style="left:1009px">Terms of Service</span>
</div>

</body>
</html>
```